Pick-n-Plate Gift Coupon

About Us-
Pick-n-Plate is a Tasmanian owned food delivery business which delivers meals from an increasing range of selected restaurants. We provide customers with quality food from reputed restaurants at reasonable delivery charges that meet the highest standards of quality and freshness.
We need some gift coupons/vouchers for our privileged customers. We need three designs which are as follows:
1) 10% OFF
2) FREE DELIVERY
3) FREE DELIVERY when you add any Wine/Beer
Coupons should have following:
Pick-n-Plate Logo
Coupon Code: __________
Note:Redeem this coupon on www.picknplate.com.au

```html
<!DOCTYPE html>
<html lang="en">
<head>
<meta charset="utf-8">
<title>Pick-n-Plate Gift Coupons</title>
<link href="https://fonts.googleapis.com/css2?family=Open+Sans:wght@400;600;700&display=swap" rel="stylesheet">
<style>
  :root {
    --ink: #111111;
    --brown: #3a1d0e;
    --orange: #f07a2c;
    --orange-soft: #f39a52;
    --frame: #2b2b2b;
    --paper: #ffffff;
  }
  * { box-sizing: border-box; margin: 0; padding: 0; }
  html, body { width: 847px; height: 1200px; overflow: hidden; background: var(--paper); }
  body { position: relative; font-family: "Open Sans", sans-serif; color: var(--ink); }

  .coupon {
    position: absolute; left: 3px; width: 841px; height: 377px;
    border: 2px solid var(--frame); background: var(--paper); overflow: hidden;
  }
  .coupon--percent { top: 3px; }
  .coupon--delivery { top: 412px; }
  .coupon--drinks { top: 820px; }

  .brand-band {
    position: absolute; left: 12px; right: 12px; top: 86px; height: 36px;
    background: linear-gradient(90deg, var(--brown) 0%, var(--brown) 35%, #9a4a1e 55%, var(--orange) 80%, var(--orange-soft) 100%);
  }
  .brand-mark {
    position: absolute; left: 14px; top: 12px; width: 128px; height: 128px;
    border-radius: 22px; background: var(--orange); border: 5px solid var(--brown);
  }
  .brand-name {
    position: absolute; left: 160px; top: 22px;
    font-size: 50px; font-weight: 700; color: var(--brown); line-height: 1;
  }
  .tagline {
    position: absolute; left: 163px; top: 90px;
    font-size: 24px; color: var(--paper); line-height: 1; letter-spacing: 0.5px;
  }
  .phone {
    position: absolute; left: 640px; top: 58px;
    font-size: 20px; color: var(--ink); display: flex; align-items: center; gap: 5px;
  }
  .phone svg { width: 16px; height: 16px; }

  .cut-line {
    position: absolute; left: 26px; top: 133px; width: 800px; height: 222px;
    border: 2px dashed var(--orange);
  }
  .headline {
    position: absolute; line-height: 1; color: var(--ink); white-space: nowrap;
    text-shadow: 8px 12px 9px rgba(0,0,0,0.55);
  }
  .headline--percent { left: 90px; top: 150px; font-size: 128px; font-weight: 600; }
  .headline--delivery { left: 56px; top: 152px; font-size: 103px; font-weight: 400; letter-spacing: -1px; }
  .coupon--drinks .headline--delivery { top: 140px; }

  .condition { position: absolute; left: 44px; top: 272px; font-size: 18px; }
  .redeem { position: absolute; left: 44px; top: 303px; font-size: 19px; }
  .code-label { position: absolute; left: 644px; top: 268px; font-size: 20px; }
  .code-box {
    position: absolute; left: 622px; top: 300px; width: 182px; height: 38px;
    border: 2px solid var(--ink); background: var(--paper);
  }
</style>
</head>
<body>

<section class="coupon coupon--percent">
  <div class="brand-band"></div>
  <div class="brand-mark"></div>
  <div class="brand-name">Pick-n-Plate</div>
  <div class="tagline">good food, delivered</div>
  <div class="phone">
    <svg viewBox="0 0 24 24" aria-hidden="true"><path fill="#111" d="M6.6 10.8a15.1 15.1 0 0 0 6.6 6.6l2.2-2.2a1 1 0 0 1 1-.25 11.4 11.4 0 0 0 3.6.57 1 1 0 0 1 1 1V20a1 1 0 0 1-1 1A17 17 0 0 1 3 4a1 1 0 0 1 1-1h3.5a1 1 0 0 1 1 1c0 1.25.2 2.45.57 3.6a1 1 0 0 1-.25 1z"/></svg>
    0400 555 218
  </div>
  <div class="cut-line"></div>
  <div class="headline headline--percent">10% OFF</div>
  <div class="redeem">Redeem this coupon on www.picknplate.com.au</div>
  <div class="code-label">Coupon Code</div>
  <div class="code-box"></div>
</section>

<section class="coupon coupon--delivery">
  <div class="brand-band"></div>
  <div class="brand-mark"></div>
  <div class="brand-name">Pick-n-Plate</div>
  <div class="tagline">good food, delivered</div>
  <div class="phone">
    <svg viewBox="0 0 24 24" aria-hidden="true"><path fill="#111" d="M6.6 10.8a15.1 15.1 0 0 0 6.6 6.6l2.2-2.2a1 1 0 0 1 1-.25 11.4 11.4 0 0 0 3.6.57 1 1 0 0 1 1 1V20a1 1 0 0 1-1 1A17 17 0 0 1 3 4a1 1 0 0 1 1-1h3.5a1 1 0 0 1 1 1c0 1.25.2 2.45.57 3.6a1 1 0 0 1-.25 1z"/></svg>
    0400 555 218
  </div>
  <div class="cut-line"></div>
  <div class="headline headline--delivery">FREE DELIVERY</div>
  <div class="redeem">Redeem this coupon on www.picknplate.com.au</div>
  <div class="code-label">Coupon Code</div>
  <div class="code-box"></div>
</section>

<section class="coupon coupon--drinks">
  <div class="brand-band"></div>
  <div class="brand-mark"></div>
  <div class="brand-name">Pick-n-Plate</div>
  <div class="tagline">good food, delivered</div>
  <div class="phone">
    <svg viewBox="0 0 24 24" aria-hidden="true"><path fill="#111" d="M6.6 10.8a15.1 15.1 0 0 0 6.6 6.6l2.2-2.2a1 1 0 0 1 1-.25 11.4 11.4 0 0 0 3.6.57 1 1 0 0 1 1 1V20a1 1 0 0 1-1 1A17 17 0 0 1 3 4a1 1 0 0 1 1-1h3.5a1 1 0 0 1 1 1c0 1.25.2 2.45.57 3.6a1 1 0 0 1-.25 1z"/></svg>
    0400 555 218
  </div>
  <div class="cut-line"></div>
  <div class="headline headline--delivery">FREE DELIVERY</div>
  <div class="condition">(When you add any Wine/Beer)</div>
  <div class="redeem">Redeem this coupon on www.picknplate.com.au</div>
  <div class="code-label">Coupon Code</div>
  <div class="code-box"></div>
</section>

</body>
</html>
```